RV Wrecking business cards v.2 first was me

So the ones in the picture are my original cards that I came up with. 😅however I kinda messed up on two things, I missed spelled my name it should be Dariel Montoya as well as the email should be Darielm@brightlanecrews.com. I would like to clean this card up and also make it pop! Something that people would remember me by and that screams DEMOLITION. As well as a card that give you a feeling of loyalty and trust. I would also like to change and remove junk hauling and add full demolition to replace it. These cards worked for a little while but I cant make that my image while handing these out. I would also like to only put down that we are located in Cedar Hollow, CA, 90000 instead of the address on the card. Also if we can have a line that states Licensed, Bonded, & Insured. With out License # 4837215

Target Market(s)

Contractors and Home owners

Industry/Entity Type

Construction specialist in Demolition

Contact Information for Business Card

R Wrecking Selective Demolition & Full Demolition Kitchens AD Preparation Bathrooms Sheds Interiors & Exteriors Demo Digging And Much More Darielll Montoya Owner our city state and zip

Font styles to use
Serif
Sans Serif
Decorative

Colors
0054AA
0677BA
7BADD7
CADEEF
E8F1F8
0094D4
00A9DD
6FCCEA
C7EBF8
E9F6FB

Requirements
Must have
• License# 4837215
Nice to have
• Trying to go with a blue and white color scheme
Should not have
• Building construction

```html
<!DOCTYPE html>
<html lang="en">
<head>
<meta charset="utf-8">
<title>RV Wrecking – Business Cards</title>
<link href="https://fonts.googleapis.com/css2?family=Oswald:wght@500;600;700&family=Montserrat:wght@400;500;600&display=swap" rel="stylesheet">
<style>
  :root {
    --stage: #3b3b3d;
    --card-white: #ffffff;
    --card-fade: #ececee;
    --card-black: #121212;
    --brand-blue: #0054aa;
    --ink: #111111;
    --muted: #2b2b2b;
    --divider: #9a9a9a;
  }
  * { box-sizing: border-box; margin: 0; padding: 0; }
  html, body {
    width: 1200px; height: 1200px; overflow: hidden;
    background: var(--stage);
  }
  .canvas {
    width: 1200px; height: 1200px;
    display: flex; flex-direction: column; align-items: center;
    justify-content: center; gap: 40px;
  }
  .card {
    width: 960px; height: 540px; border-radius: 44px;
    position: relative; overflow: hidden;
    border-bottom: 6px solid var(--brand-blue);
    box-shadow: 0 18px 40px rgba(0,0,0,.45);
  }

  /* Front */
  .card--front {
    background: linear-gradient(180deg, var(--card-white) 55%, var(--card-fade) 100%);
    padding: 56px 70px 0 70px;
  }
  .brand {
    display: flex; align-items: center; gap: 18px;
  }
  .brand__dot {
    width: 44px; height: 44px; border-radius: 50%;
    background: var(--brand-blue); flex: none;
  }
  .brand__name {
    font-family: "Oswald", sans-serif; font-weight: 700;
    font-size: 84px; line-height: 1; letter-spacing: 2px;
    color: var(--brand-blue); text-transform: uppercase;
  }
  .brand__license {
    font-family: "Oswald", sans-serif; font-weight: 600;
    font-size: 22px; letter-spacing: 3px; color: var(--ink);
    margin: 6px 0 0 62px;
  }
  .services {
    margin-top: 26px; text-align: center;
    font-family: "Oswald", sans-serif; text-transform: uppercase;
  }
  .services__headline {
    color: var(--brand-blue); font-weight: 600; font-size: 28px; letter-spacing: .5px;
  }
  .services__list {
    color: var(--ink); font-weight: 600; font-size: 28px; line-height: 1.25;
  }
  .rule {
    height: 2px; background: var(--brand-blue);
    margin: 22px -10px 0 -10px;
  }
  .details {
    display: flex; align-items: center; margin-top: 24px;
  }
  .person { flex: 1; font-family: "Montserrat", sans-serif; }
  .person__name {
    color: var(--brand-blue); font-weight: 600; font-size: 34px; letter-spacing: -.5px;
    text-transform: uppercase;
  }
  .person__role { color: var(--muted); font-size: 18px; font-weight: 500; margin-top: 2px; }
  .person__claim { color: var(--brand-blue); font-size: 22px; margin-top: 14px; }
  .person__license { color: var(--muted); font-size: 22px; }
  .details__divider {
    width: 1px; height: 130px; background: var(--divider); margin: 0 36px;
  }
  .contact { flex: 1.15; font-family: "Montserrat", sans-serif; list-style: none; }
  .contact__item {
    display: flex; align-items: center; gap: 12px;
    font-size: 20px; color: var(--muted); line-height: 1.7;
  }
  .contact__icon { width: 22px; height: 22px; fill: var(--brand-blue); flex: none; }

  /* Back */
  .card--back {
    background: var(--card-black);
    display: flex; flex-direction: column; align-items: center; justify-content: center;
  }
  .card--back .brand__name { font-size: 120px; }
  .card--back .brand__dot { width: 62px; height: 62px; }
  .card--back .brand__license {
    color: var(--card-white); font-size: 30px; letter-spacing: 5px; margin: 10px 0 0 80px;
  }
</style>
</head>
<body>
<main class="canvas">

  <section class="card card--front" aria-label="Business card front">
    <div class="brand">
      <span class="brand__dot"></span>
      <span class="brand__name">RV Wrecking</span>
    </div>
    <p class="brand__license">LICENSE#4837215</p>

    <div class="services">
      <p class="services__headline">Selective Demolition &amp; Full Demolition</p>
      <p class="services__list">Kitchens • ADU Preparation • Bathrooms • Sheds<br>Interiors &amp; Exteriors Demo • Digging and Much More</p>
    </div>

    <div class="rule"></div>

    <div class="details">
      <div class="person">
        <p class="person__name">Dariel Montoya</p>
        <p class="person__role">OWNER</p>
        <p class="person__claim">Licensed, Bonded &amp; Insured</p>
        <p class="person__license">License# 4837215</p>
      </div>
      <div class="details__divider"></div>
      <ul class="contact">
        <li class="contact__item">
          <svg class="contact__icon" viewBox="0 0 24 24"><path d="M6.6 10.8a15.1 15.1 0 0 0 6.6 6.6l2.2-2.2a1 1 0 0 1 1-.25 11.4 11.4 0 0 0 3.6.57 1 1 0 0 1 1 1V20a1 1 0 0 1-1 1A17 17 0 0 1 3 4a1 1 0 0 1 1-1h3.5a1 1 0 0 1 1 1c0 1.25.2 2.45.57 3.57a1 1 0 0 1-.25 1z"/></svg>
          (949) 555-0183
        </li>
        <li class="contact__item">
          <svg class="contact__icon" viewBox="0 0 24 24"><path d="M2 5h20v14H2z M2 5l10 8 10-8" fill="none" stroke="var(--brand-blue)" stroke-width="2.4"/></svg>
          Darielm@brightlanecrews.com
        </li>
        <li class="contact__item">
          <svg class="contact__icon" viewBox="0 0 24 24"><path d="M12 2a7 7 0 0 0-7 7c0 5.2 7 13 7 13s7-7.8 7-13a7 7 0 0 0-7-7zm0 9.5A2.5 2.5 0 1 1 12 6.5a2.5 2.5 0 0 1 0 5z"/></svg>
          Cedar Hollow, CA, 90000
        </li>
      </ul>
    </div>
  </section>

  <section class="card card--back" aria-label="Business card back">
    <div class="brand">
      <span class="brand__dot"></span>
      <span class="brand__name">RV Wrecking</span>
    </div>
    <p class="brand__license">LICENSE#4837215</p>
  </section>

</main>
</body>
</html>
```